New Wordpress Design Project

The website is my name tessamaybrook.com

I need a website design that will be graphically pleasing and have a crisp feel to it. I am a business and personal coach and have many different niches that I work with. I am looking for the central site to describe who I am and how I help people - I help people "wake up" to make conscious choices in their lives. I use hypnosis but do not want it to be esoteric, I ground the hypnosis and base it in science of how people can manage their state to reach their full potential in their lives and in business. I work one on one but also do public speaking and recently started to do trainings with corporations, helping people improve their business. I am looking at this as a merge of hypnosis and other tools with the business or corporate world - based in science - neuroplasticity, brain training etc. I will be helping people to overcome anxiety and stress, limiting beliefs, controlling and choosing habits that will work for them, fears and phobias, golf/sports improvement, weight loss.

Really helping people to center back with themselves, to not be so caught up in their head but drop into their heart and with what is really going on. My mission is to connect them back with themselves, using language, state and conscious choice.

I work online with entrepreneurs helping them to get unstuck, move past fears and limiting beliefs to create the business of their dreams.

I added a file of what I am envisioning on the right hand side of my site to show people the different niches I am involved with.

Some sites that I like www.gretavanholt.com www.corinnemaddox.org http://www.judekestrel.com/ , Details for my new Wordpress Design Project will be added soon. , The website is my name tessamaybrook.com

the square boxes graphic below is similar to one that I will be making for a page on my site for clarity and crispness. But will be creating it more in the teal color.

Target Market(s)

My target market are both male and female 30-50 either entreprenuers/business people

Industry/Entity Type

Training

Requirements
Must have
• A video with an opt in box
My background color is teal/blue (see below file)
Social media links

```html
<!DOCTYPE html>
<html lang="en">
<head>
<meta charset="utf-8">
<title>Tessa May Brook — Optimising Your Mindset for Entrepreneurial Success</title>
<link rel="stylesheet" href="https://fonts.googleapis.com/css2?family=Open+Sans:ital,wght@0,400;0,600;0,700;1,400&family=Raleway:wght@400;500;600;700&family=Libre+Baskerville:ital@1&display=swap">
<style>
:root{
  --teal:#1f9ba4;
  --teal-dark:#1b6a72;
  --teal-deep:#17585f;
  --ink:#333;
  --muted:#777;
  --line:#e3e3e3;
  --orange:#f27a1a;
  --yellow:#f4c20d;
  --bar:#2a2a2a;
  --band:#ececec;
  --white:#fff;
}
*{box-sizing:border-box;margin:0;padding:0}
html,body{width:1200px;height:2400px;overflow:hidden}
body{position:relative;background:var(--white);font-family:"Open Sans",Arial,sans-serif;color:var(--ink);font-size:13px}
.abs{position:absolute}

/* top strip */
.util-bar{left:0;top:0;width:1200px;height:28px;background:var(--bar)}
.util-links{right:175px;top:6px;display:flex;gap:14px;font-size:11px;color:#ddd}
.hero-band{left:0;top:28px;width:1200px;height:308px;background:var(--teal)}

/* brand */
.brand{left:175px;top:50px;display:flex;align-items:center;gap:12px}
.brand-mark{width:48px;height:48px;background:var(--yellow)}
.brand-name{font-family:"Raleway",sans-serif;font-weight:700;font-size:40px;color:var(--white);letter-spacing:-.5px}
.brand-tag{left:238px;top:102px;font-size:12px;color:#e6f6f7;font-style:italic}
.follow{right:175px;top:52px;text-align:right;color:var(--white);font-family:"Raleway",sans-serif;font-size:22px}
.social{display:flex;gap:6px;justify-content:flex-end;margin-top:8px}
.social span{width:28px;height:28px;border-radius:50%;background:var(--white)}

/* nav */
.nav{left:175px;top:132px;width:850px;height:44px;background:var(--teal-dark);display:flex;align-items:center}
.nav-home{width:44px;height:44px;background:var(--yellow);display:flex;align-items:center;justify-content:center}
.nav a{color:var(--white);text-decoration:none;font-weight:600;font-size:15px;margin-left:28px}
.nav-search{margin-left:auto;margin-right:12px;width:190px;height:26px;background:var(--white);font-size:11px;color:#555;padding:5px 8px}

/* video + opt-in */
.video{left:175px;top:192px;width:569px;height:276px;background:linear-gradient(135deg,#dfe8ea,#c7a98c 55%,#7d9aa0)}
.video-play{left:253px;top:95px;width:80px;height:80px;border-radius:50%;border:4px solid rgba(255,255,255,.85)}
.video-caption{left:0;bottom:0;width:569px;height:44px;background:rgba(0,0,0,.55);color:var(--white);font-size:20px;padding:9px 14px;display:flex;justify-content:space-between}
.optin{left:756px;top:192px;width:269px;height:276px;background:var(--bar);color:var(--white);text-align:center}
.optin-art{margin:0 auto;width:269px;height:140px;background:linear-gradient(180deg,#fff,#f4ead8);}
.optin p{font-size:10.5px;font-weight:600;padding:10px 18px 6px;line-height:1.35}
.optin-input{margin:0 auto;width:230px;height:22px;background:var(--white);color:#555;font-size:10px;text-align:left;padding:4px 8px}
.btn{display:inline-block;background:var(--orange);color:var(--white);font-weight:700;font-size:11px;padding:5px 18px;margin-top:8px}

/* intro */
.intro-title{left:175px;top:502px;font-family:"Raleway",sans-serif;font-size:24px;color:var(--teal);font-weight:500;white-space:nowrap}
.intro-art{left:175px;top:540px;width:260px;height:112px;background:linear-gradient(180deg,#fafafa,#eee)}
.intro-text{left:448px;top:500px;width:577px;font-size:12.5px;line-height:1.45;color:#444}
.intro-text p{margin-bottom:10px}
.intro-meta{font-size:10.5px;color:var(--teal)}
.read-more{float:right;color:var(--orange);font-weight:700;font-size:10px}

/* posts */
.post{width:281px}
.post-img{width:281px;height:180px;box-shadow:0 0 0 6px #f3f3f3}
.post h3{font-family:"Raleway",sans-serif;font-weight:500;font-size:17px;color:var(--teal);margin-top:16px;line-height:1.25}
.post-meta{font-size:10.5px;font-weight:700;margin:6px 0}
.post-excerpt{font-size:10.5px;line-height:1.4;color:#555}
.share{display:flex;gap:6px;align-items:center;margin-top:10px}
.share span{font-size:9px;border:1px solid #ccc;padding:1px 5px;color:#444}
.share .plus{margin-left:auto;width:16px;height:16px;background:var(--teal);border:none}

/* sidebar */
.widget{left:756px;width:269px;border:1px solid var(--line);background:var(--white);overflow:hidden}
.signup{top:708px;height:182px;padding:12px 14px}
.signup h4{font-family:"Raleway",sans-serif;font-size:22px;font-weight:500;color:var(--teal)}
.signup small{font-size:11px;display:block;margin:4px 0 8px;width:140px}
.signup-art{right:0;top:0;width:82px;height:84px;background:linear-gradient(135deg,#f0d5c6,#d8574a)}
.field{height:22px;border:1px solid #ccc;font-size:10px;padding:4px 8px;margin-bottom:6px;width:240px}
.field.short{width:150px}
.community{top:900px;height:228px;padding:10px}
.community h4{font-family:"Raleway",sans-serif;font-size:19px;font-weight:500;color:var(--teal);margin-bottom:8px}
.feed-item{display:flex;gap:8px;margin-bottom:10px}
.avatar{width:36px;height:36px;flex:none;background:linear-gradient(135deg,#e9d2b2,#a98a6a)}
.feed-item b{font-size:10.5px;color:#2d5c9a}
.feed-item p{font-size:10px;line-height:1.35}
.feed-item i{display:block;font-size:9px;color:var(--muted);font-style:normal;margin-top:3px}
.about{top:1152px;height:372px;background:var(--teal-deep);border:none;color:var(--white)}
.about-img{width:269px;height:372px;background:linear-gradient(180deg,#6f8d55,#a8c07a 45%,#3d5a36)}
.about-text{left:12px;top:196px;width:245px;background:rgba(0,0,0,.55);font-size:11.5px;line-height:1.35;padding:8px 10px}
.about-cta{left:0;bottom:0;width:269px;height:62px;background:var(--teal);font-family:"Raleway",sans-serif;font-size:19px;line-height:1.15;text-align:center;padding-top:8px}
.recent{top:1548px;height:216px;padding:12px}
.recent h4{font-family:"Raleway",sans-serif;font-size:20px;font-weight:500;color:var(--teal);margin-bottom:10px}
.recent li{list-style:none;font-size:11px;padding:5px 0;border-bottom:1px solid #f1f1f1}
.recent li.active{color:var(--teal);text-decoration:underline}

/* testimonials */
.testi-title{left:0;top:1858px;width:1200px;text-align:center;font-family:"Raleway",sans-serif;font-size:21px;color:var(--teal);font-weight:500}
.testi-band{left:0;top:1896px;width:1200px;height:300px;background:var(--band)}
.testi-photo{left:552px;top:1918px;width:96px;height:110px;background:var(--white);border:1px solid #ccc;padding:8px}
.testi-photo div{width:100%;height:100%;background:linear-gradient(180deg,#c9b9a3,#5a4a3a)}
.testi-quote{left:270px;top:2048px;width:660px;text-align:center;font-family:"Libre Baskerville",Georgia,serif;font-style:italic;font-size:12.5px;line-height:1.6;color:#444}
.testi-by{display:block;margin-top:10px;font-family:"Open Sans",sans-serif;font-style:normal;font-weight:600}

.follow-box{left:438px;top:2234px;width:324px;height:60px;border:1px solid var(--line);border-radius:6px;display:flex;align-items:center;justify-content:center;gap:12px;font-size:19px;color:#555}
.follow-box b{color:#c8232c;font-weight:700}

.footer{left:0;top:2322px;width:1200px;height:54px;background:var(--teal);display:flex;justify-content:center;align-items:center;gap:12px}
.footer span{width:24px;height:24px;border-radius:50%;background:var(--white)}
.copyright{left:0;top:2376px;width:1200px;height:24px;background:var(--bar);color:#ddd;font-size:10px;text-align:center;padding-top:5px;font-weight:600}
</style>
</head>
<body>

<div class="abs util-bar"></div>
<nav class="abs util-links"><span>Lorem</span><span>Ipsum</span><span>Dolor</span><span>Sample</span><span>Texts</span></nav>
<div class="abs hero-band"></div>

<div class="abs brand"><span class="brand-mark"></span><span class="brand-name">TessaMayBrook</span></div>
<div class="abs brand-tag">Optimising Your Mindset for Entrepreneurial Success</div>
<div class="abs follow">Follow TessaMay
  <div class="social"><span></span><span></span><span></span><span></span><span></span></div>
</div>

<nav class="abs nav">
  <div class="nav-home"><svg width="20" height="18" viewBox="0 0 20 18"><path d="M10 1 1 9h3v8h5v-5h2v5h5V9h3z" fill="#fff"/></svg></div>
  <a>My Story</a><a>Coaching</a><a>Testimonials</a><a>Contact</a>
  <div class="nav-search">Enter Search</div>
</nav>

<section class="abs video" role="img" aria-label="Video still of the coach smiling outdoors">
  <div class="abs video-play"><svg width="72" height="72" viewBox="0 0 72 72"><path d="M29 22 52 36 29 50z" fill="rgba(255,255,255,.85)"/></svg></div>
  <div class="abs video-caption"><span>Click PLAY For a Special Message from Tessa May...</span><svg width="16" height="22" viewBox="0 0 16 22"><path d="M2 3 14 11 2 19z" fill="#fff"/></svg></div>
</section>
<aside class="abs optin">
  <div class="optin-art" role="img" aria-label="Book and DVD package"></div>
  <p>Get My Instant Life changing Book &amp; DVD, please use your email to reach me. I'll get to you with the solution.</p>
  <div class="optin-input">Enter Email</div>
  <span class="btn">I WANT IT</span>
</aside>

<h2 class="abs intro-title">What is stopping you?</h2>
<div class="abs intro-art" role="img" aria-label="Sketch of a line from point A to point B"></div>
<div class="abs intro-text">
  <p>If you could change anything in your life right now, what would it be? And why haven't you done it yet? If you're like most of us, the answer lies in your existing beliefs.<br>We often forget the powerful role our beliefs play in creating what we want. We can visualize, affirm, set goals, and work hard till the cows come home — but if we don't believe something is possible, we will resist the formation of it in our lives.</p>
  <p>The good news is, once you understand how your beliefs are holding you back, you have full control over changing those limiting beliefs — and your life will change in awesome and spectacular ways!</p>
  <div class="intro-meta">Categories: Limiting Beliefs · Tags: beliefs, change, desire, Limiting beliefs, money <span class="read-more">READ MORE</span></div>
</div>

<!-- posts -->
<article class="abs post" style="left:175px;top:708px">
  <div class="post-img" role="img" aria-label="Man asleep at his desk" style="background:linear-gradient(180deg,#e9eef1,#b9c4cc)"></div>
  <h3>Are you sleepwalking through life?</h3>
  <div class="post-meta">Tue 20 Mar 2013 | Tessa May</div>
  <p class="post-excerpt">Do you keep hearing everyone talking about authenticity, knowing who you are and not really worrying about what others think about it?</p>
  <div class="share"><span>Like</span><span>+1</span><span>Share</span><span class="plus"></span></div>
</article>
<article class="abs post" style="left:468px;top:708px">
  <div class="post-img" role="img" aria-label="Businessman aiming a bow at the sky" style="background:linear-gradient(180deg,#cfe3f0,#7fa3bb)"></div>
  <h3>Set Your Goals on Fire!</h3>
  <div class="post-meta">Tue 20 Mar 2013 | Tessa May</div>
  <p class="post-excerpt">I'm sure everyone reading this has set a goal, whether it was New Year's Eve goals, fitness or monetary goals and come up far short of meeting them.</p>
  <div class="share"><span>Like</span><span>+1</span><span>Share</span><span class="plus"></span></div>
</article>
<article class="abs post" style="left:175px;top:1084px">
  <div class="post-img" role="img" aria-label="Woman with raised arms in a sunlit field" style="background:linear-gradient(180deg,#f7f1c8,#c9c25a)"></div>
  <h3>Emotional Resilience is Good For You</h3>
  <div class="post-meta">Tue 20 Mar 2013 | Tessa May</div>
  <p class="post-excerpt">Do you keep hearing everyone talking about authenticity, knowing who you are and not really worrying about what others think about it?</p>
  <div class="share"><span>Like</span><span>+1</span><span>Share</span><span class="plus"></span></div>
</article>
<article class="abs post" style="left:468px;top:1084px">
  <div class="post-img" role="img" aria-label="Glowing brain illustration" style="background:radial-gradient(circle at 50% 55%,#f0a24a,#2e4f8c 70%)"></div>
  <h3>Neuroplasticity. What is it and what can it do for you?</h3>
  <div class="post-meta">Tue 20 Mar 2013 | Tessa May</div>
  <p class="post-excerpt">I'm sure everyone reading this has set a goal, whether it was New Year's Eve goals, fitness or monetary goals and come up far short of meeting them.</p>
  <div class="share"><span>Like</span><span>+1</span><span>Share</span><span class="plus"></span></div>
</article>
<article class="abs post" style="left:175px;top:1476px">
  <div class="post-img" role="img" aria-label="Golden key in a white stone lock" style="background:linear-gradient(180deg,#fafafa,#d8d8d8)"></div>
  <h3>Can you really rewire your brain for success?</h3>
  <div class="post-meta">Tue 20 Mar 2013 | Tessa May</div>
  <p class="post-excerpt">Do you keep hearing everyone talking about authenticity, knowing who you are and not really worrying about what others think about it?</p>
  <div class="share"><span>Like</span><span>+1</span><span>Share</span><span class="plus"></span></div>
</article>
<article class="abs post" style="left:468px;top:1476px">
  <div class="post-img" role="img" aria-label="Cupped hands holding a stone reading hope" style="background:linear-gradient(180deg,#9aa1a6,#4f565b)"></div>
  <h3>Having an Optimistic Mindset Can Help</h3>
  <div class="post-meta">Tue 20 Mar 2013 | Tessa May</div>
  <p class="post-excerpt">I'm sure everyone reading this has set a goal, whether it was New Year's Eve goals, fitness or monetary goals and come up far short of meeting them.</p>
  <div class="share"><span>Like</span><span>+1</span><span>Share</span><span class="plus"></span></div>
</article>

<!-- sidebar -->
<aside class="abs widget signup">
  <div class="abs signup-art" role="img" aria-label="Stressed woman holding her head"></div>
  <h4>Sign Up for</h4>
  <small>FREE anxiety management course</small>
  <div class="field short">Name</div>
  <div class="field">Email</div>
  <div style="text-align:right"><span class="btn" style="margin-top:2px">START NOW</span></div>
</aside>
<aside class="abs widget community">
  <h4>Join the Community...</h4>
  <div class="feed-item"><div class="avatar" role="img" aria-label="Profile photo"></div><div><b>Tessa May Brook</b><p style="margin-top:4px"><span style="background:#4a66a0;color:#fff;padding:0 4px;font-size:9px">Like</span> 86</p></div></div>
  <div class="feed-item"><div class="avatar" role="img" aria-label="Profile photo"></div><div><b>Tessa May Brook</b><p>Great news shared with the community today, read the full post.</p><i>January 21 at 6:15pm</i></div></div>
  <div class="feed-item"><div class="avatar" role="img" aria-label="Profile photo"></div><div><b>Tessa May Brook</b><p>"Happiness is genuine satisfaction with your present experience" Warren Ellcott</p><i>January 21 at 6:15pm</i></div></div>
</aside>
<aside class="abs widget about">
  <div class="about-img" role="img" aria-label="Portrait of the coach in a garden"></div>
  <p class="abs about-text">I am an entrepreneur and coach. I help you get your Inner-Game working so you have Outer-Game success! I have an obsession with the mechanics of our thoughts and actions and the neuroscience behind it.</p>
  <div class="abs about-cta">Meet Tessa May and<br>Connect!</div>
</aside>
<aside class="abs widget recent">
  <h4>Recent Post</h4>
  <ul>
    <li>What is stopping you?</li>
    <li>Are you sleepwalking through life?</li>
    <li>Set Your Goals on Fire!</li>
    <li class="active">Emotional Resilience is Good For You</li>
    <li>Neuroplasticity. What is it and what can it do for you?</li>
  </ul>
</aside>

<!-- testimonials -->
<h2 class="abs testi-title">Client Testimonials</h2>
<section class="abs testi-band">
  <svg class="abs" style="left:345px;top:72px" width="24" height="60" viewBox="0 0 24 60"><path d="M20 2 4 30l16 28" fill="none" stroke="#c9c9c9" stroke-width="3"/></svg>
  <svg class="abs" style="left:831px;top:72px" width="24" height="60" viewBox="0 0 24 60"><path d="M4 2l16 28L4 58" fill="none" stroke="#c9c9c9" stroke-width="3"/></svg>
</section>
<div class="abs testi-photo"><div role="img" aria-label="Client headshot"></div></div>
<blockquote class="abs testi-quote">Tessa May was a huge help to me in dealing with some inner-game issues related to my business. She helped me get clear on exactly what I needed to do to move forward and overcome those obstacles. And best of all, she held me accountable to make sure that I took the action and got the desired results!<span class="testi-by">~ Dean Hollis</span></blockquote>

<div class="abs follow-box">Follow me on <b>Pinwall</b></div>

<footer class="abs footer"><span></span><span></span><span></span><span></span><span></span></footer>
<div class="abs copyright">Copyright © 2014 tessamaybrook.com</div>

</body>
</html>
```